eBook Cover_H. Vollmar-Tessen
Schnell und zuverlässoig,Änderungswünsche wurden umgehend ausgeführt. Vielen Dank für das tolle Cover zu meinem ersten Buch!
Zielgruppe
freie Roman-Autorin (Erstlingswerk)
Zielgruppe: Lesende (Erwachsene), Frauen
Charakterisierung: magisch-realistischer Familienroman, spielt im Europa der Jetzt-Zeit
Aufgabenstellung
Im ersten Schritt geht es um ein Cover für ein eBook, das aber bei Bedarf als Book on Demand gedruckt werden soll. Es wird daher später Anforderung bzgl. Dicke / Umfang des gedruckten Buches und einer Rückseite geben. Das gewählte Design soll dann dahingehend überarbeitet und finale Druckdaten zur Verfügung gestellt werden. Dies soll von vornherein berücksichtigt werden und im Preis enthalten sein.
Titel: Nebel über Glas, Funken im Moor
Autorinnenname: Henrike Vollmar-Tessen
des weiteren auf dem Cover: Roman

```html
<!DOCTYPE html>
<html lang="de">
<head>
<meta charset="utf-8">
<title>Nebel über Glas, Funken im Moor – eBook Cover</title>
<link href="https://fonts.googleapis.com/css2?family=Cinzel:wght@400;600;700&display=swap" rel="stylesheet">
<style>
  :root {
    --page: #ffffff;
    --cover-dark: #241818;
    --cover-deep: #3a1f1c;
    --bloom-red: #b8281c;
    --bloom-coral: #e0644a;
    --bloom-light: #f3c1a8;
    --type: #f4efe9;
  }
  html, body {
    margin: 0;
    padding: 0;
    width: 848px;
    height: 1200px;
    overflow: hidden;
    background: var(--page);
  }
  .canvas {
    position: relative;
    width: 848px;
    height: 1200px;
    background: var(--page);
  }
  .cover {
    position: absolute;
    left: 127px;
    top: 107px;
    width: 606px;
    height: 895px;
    background: radial-gradient(ellipse at 50% 45%, var(--cover-deep) 0%, var(--cover-dark) 70%);
    overflow: hidden;
    font-family: "Cinzel", "Times New Roman", serif;
    color: var(--type);
  }
  .cover__art {
    position: absolute;
    left: 110px;
    top: 60px;
    width: 440px;
    height: 620px;
    background:
      radial-gradient(ellipse 30% 18% at 48% 38%, var(--bloom-light) 0%, rgba(243,193,168,0) 100%),
      radial-gradient(ellipse 28% 16% at 38% 62%, rgba(243,193,168,0.8) 0%, rgba(243,193,168,0) 100%),
      radial-gradient(ellipse 50% 45% at 55% 40%, var(--bloom-coral) 0%, rgba(224,100,74,0) 100%),
      radial-gradient(ellipse 48% 50% at 50% 55%, var(--bloom-red) 0%, rgba(184,40,28,0) 100%);
    filter: blur(4px);
  }
  .cover__author {
    position: absolute;
    top: 32px;
    left: 0;
    right: 0;
    text-align: center;
    font-size: 27px;
    font-weight: 700;
    letter-spacing: 0.5px;
  }
  .cover__title {
    position: absolute;
    top: 700px;
    left: 0;
    right: 0;
    margin: 0;
    text-align: center;
    font-weight: 400;
    line-height: 68px;
    font-size: 58px;
    letter-spacing: -0.5px;
  }
  .cover__title .joiner {
    font-size: 24px;
    letter-spacing: 0;
  }
  .cover__genre {
    position: absolute;
    top: 838px;
    left: 0;
    right: 0;
    text-align: center;
    font-size: 26px;
    font-weight: 700;
  }
</style>
</head>
<body>
<div class="canvas">
  <section class="cover">
    <div class="cover__art" role="img" aria-label="Gemalte rote und lachsfarbene Blüten auf dunklem Grund"></div>
    <div class="cover__author">HENRIKE VOLLMAR-TESSEN</div>
    <h1 class="cover__title">
      NEBEL<span class="joiner">ÜBER</span>GLAS,<br>
      FUNKEN<span class="joiner">IM</span>MOOR
    </h1>
    <div class="cover__genre">ROMAN</div>
  </section>
</div>
</body>
</html>
```